Weather of the Heart Is the Ledger A Novel by Carl Whitby and Martin Holloway

Weather of the Heart Is the Ledger is a business novel about leadership, follower-ship, resilience, and insight.
It follows a high-performing executive whose conventional management tools and techniques stop working during a professional crisis. His transformation does not come from new strategies or tactics, but from a fundamentally different understanding of how mindset shapes performance, decision-making, leadership and follower-ship. Through the course of the book, the executive, his team, and his customers realize that “State of Mind” (healthy psychological functioning) is the horsepower that drives business and life.
This is not a self-help book, textbook, or memoir. It is thoughtful business fiction with philosophical depth.

Introduction/Preface for the novel:
We wrote this book because something profound changed the way we live, work, and lead. Over the course of several decades - across boardrooms, high-stakes corporate challenges, private practice, and moments of quiet personal insight - we began to see a deeper truth about the human experience. It was a truth that, once seen, dramatically improved the quality of our lives, and the lives of the people with whom we worked.
That truth comes from understanding the Three Principles of Mind, Consciousness, and Thought, as discovered and first articulated by the philosopher and theosopher, Edwin Thorley. Though simple, these Principles point to something universally powerful—how all people experience life from the inside out. When understood, they reveal a level of clarity, resilience, and well-being that can transform not only individuals, but entire organizations.
At first, we tried to write a traditional business book—a primer designed to share how understanding the Principles can lead to more grounded, wise, and effective leadership—without the need for techniques or tools. But as we wrote, we found ourselves returning again and again to stories. Real stories. Composite stories. Fictional ones. We realized that the best way to share this understanding wasn’t through frameworks or prescriptive advice. It was through story.
So, we created one big story.
This novel is the result. Though fictional, it is inspired by real patterns, real shifts, and real struggles we’ve lived through and witnessed over decades of work, together and separately. The characters are inventions, but their experiences are familiar. We’ve watched people just like them transform—from confusion to clarity, from fear to resilience, from burnout to wisdom.
Our hope is that this book moves you—not just as a story, but as an experience. We believe that the ideas woven into Owen Castell’s journey can help anyone live with greater ease, purpose, and peace of mind. Whether you lead a Fortune 500 company or a family of five, what’s offered here is for you.
And if something in this story helps you see your own life with fresh eyes, then the book has done its job.
Welcome to the journey.
—Carl & Martin

Target Market(s)

• Senior leaders, executives, and high-potential managers • Business professionals experiencing pressure, burnout, or diminishing returns from traditional leadership approaches • Leadership coaches and organizational consultants • Readers of intelligent, reflective business fiction or non-business people who are interested in what makes people tick — and achieve their highest potential Tone should appeal to serious, experienced professionals, not beginners or hype-seekers.

Industry/Entity Type

• Business / Leadership / Psychology • Business Fiction • Leadership Novel

Font styles to use
Serif

Colors
0054AA
0677BA
7BADD7
CADEEF
E8F1F8

Requirements
Must have
• We are looking for metaphorical representations of: • A fork in the road • A deviation from the conventional path (that makes all the difference) • One element choosing a different direction—not running away, not rebelling, just seeing differently Think quiet insight, not drama. Must-Haves • Clear, legible title at thumbnail size • A visual metaphor for choice or alternate thinking • Professional, credible aesthetic • Obvious that this is fiction (a novel), not a textbook • Clean typography (no clutter)
Nice to have
• • A sense of motion or transition • Minimalist or restrained color palette • One accent element that signifies insight or departure from convention • Timeless design (should still feel current in 5 or 10 years)
Should not have
• • Literal business clichés (gears, ladders, chess pieces, lightbulbs, compasses, eagles) • Stock-photo people in suits • “Hero CEO” imagery • Overly mystical or “woo-woo” visuals • Aggressive, macho, or hustle-culture tone • Anything cartoonish or silly

```html
<!DOCTYPE html>
<html lang="en">
<head>
<meta charset="utf-8">
<title>Weather of the Heart Is the Ledger — A Novel</title>
<link rel="stylesheet" href="https://fonts.googleapis.com/css2?family=Cormorant+Garamond:wght@600;700&family=Cinzel:wght@400&display=swap">
<style>
  :root {
    --blue-deep: #0054AA;
    --blue-mid: #0677BA;
    --blue-soft: #7BADD7;
    --blue-pale: #CADEEF;
    --blue-mist: #E8F1F8;
    --white: #ffffff;
    --credit-panel: rgba(0, 84, 170, 0.9);
  }
  * { margin: 0; padding: 0; box-sizing: border-box; }
  html, body { width: 800px; height: 1200px; overflow: hidden; background: var(--white); }
  .cover {
    position: relative;
    width: 800px;
    height: 1200px;
    overflow: hidden;
    background: linear-gradient(180deg, var(--blue-mist) 0%, var(--blue-mist) 35%, var(--blue-pale) 60%, var(--blue-soft) 100%);
  }
  .landscape {
    position: absolute;
    inset: 0;
    width: 800px;
    height: 1200px;
  }
  .title {
    position: absolute;
    top: 74px;
    left: 0;
    width: 800px;
    text-align: center;
    font-family: "Cormorant Garamond", serif;
    font-weight: 700;
    font-size: 58px;
    line-height: 1;
    letter-spacing: 1px;
    text-transform: uppercase;
    color: var(--blue-deep);
  }
  .subtitle {
    position: absolute;
    top: 162px;
    left: 0;
    width: 800px;
    text-align: center;
    font-family: "Cormorant Garamond", serif;
    font-weight: 600;
    font-size: 34px;
    line-height: 1;
    letter-spacing: 4px;
    text-transform: uppercase;
    color: var(--blue-mid);
  }
  .credit {
    position: absolute;
    left: 191px;
    top: 1022px;
    width: 486px;
    height: 92px;
    background: var(--credit-panel);
    color: var(--white);
    font-family: "Cinzel", serif;
    text-align: center;
    text-transform: uppercase;
  }
  .credit-label {
    display: block;
    font-size: 54px;
    line-height: 1;
    padding-top: 8px;
    letter-spacing: 1px;
  }
  .credit-authors {
    display: block;
    font-size: 19px;
    line-height: 1;
    margin-top: 5px;
    letter-spacing: 0.3px;
  }
</style>
</head>
<body>
  <main class="cover">
    <svg class="landscape" viewBox="0 0 800 1200" aria-hidden="true">
      <path class="hill-far" d="M0 610 C 180 560, 320 590, 460 570 C 600 550, 700 580, 800 560 L800 1200 L0 1200 Z" fill="#CADEEF"/>
      <path class="hill-near" d="M0 660 C 200 630, 380 660, 560 640 C 680 628, 750 645, 800 640 L800 1200 L0 1200 Z" fill="#A9CAE6"/>
      <path class="road-main" d="M150 1200 C 260 1000, 430 820, 505 645 L 530 645 C 525 820, 600 1000, 660 1200 Z" fill="#E8F1F8"/>
      <path class="road-branch" d="M355 905 C 310 800, 260 720, 225 655 L 242 655 C 290 725, 360 810, 420 880 Z" fill="#E8F1F8"/>
      <path class="road-centre" d="M405 1200 C 440 1000, 500 820, 517 645" fill="none" stroke="#7BADD7" stroke-width="4" stroke-dasharray="18 14"/>
      <path class="branch-accent" d="M385 895 C 330 800, 280 720, 234 655" fill="none" stroke="#0054AA" stroke-width="4" stroke-linecap="round"/>
      <circle class="insight-point" cx="234" cy="652" r="6" fill="#0054AA"/>
    </svg>
    <h1 class="title">Weather of the Heart</h1>
    <p class="subtitle">Is the Ledger</p>
    <div class="credit">
      <span class="credit-label">A Novel By</span>
      <span class="credit-authors">Carl Whitby and Martin Holloway</span>
    </div>
  </main>
</body>
</html>
```